Cedar Hall letterhead

We changed our name and logo now need letterhead.
3-4/72 Harlow Street Rosedale 2199
www.cedarhall.org.au
info@cedarhall.org.au
ph: 02 97584120

At this stage, we are preferencing Design #: 5398880 and Design #5401338

```html
<!DOCTYPE html>
<html lang="en">
<head>
<meta charset="utf-8">
<title>Cedar Hall Stationery</title>
<link rel="stylesheet" href="https://fonts.googleapis.com/css2?family=Lato:wght@300;400&family=Oswald:wght@300;400&display=swap">
<style>
  :root {
    --backdrop: #4c545e;
    --paper: #ffffff;
    --ink: #1f2328;
    --brand: #7d8c9a;
    --brand-dark: #5f6d7a;
    --envelope-back: #7b8896;
    --rule: #c9ced3;
  }
  * { box-sizing: border-box; margin: 0; padding: 0; }
  html, body { width: 1200px; height: 1000px; overflow: hidden; }
  body {
    background: var(--backdrop);
    font-family: "Lato", sans-serif;
    color: var(--ink);
    position: relative;
  }
  .sheet { position: absolute; background: var(--paper); box-shadow: 0 6px 18px rgba(0,0,0,.35); }

  .brand-mark { display: flex; align-items: center; gap: 8px; }
  .brand-mark .dot { border-radius: 50%; background: var(--brand); flex: none; }
  .brand-mark .name {
    font-family: "Lato", sans-serif; font-weight: 300;
    color: var(--brand-dark); text-transform: uppercase; letter-spacing: .08em; line-height: 1;
  }

  .contact {
    font-family: "Oswald", sans-serif; font-weight: 400;
    text-transform: uppercase; letter-spacing: .04em; color: var(--ink); line-height: 1.35;
  }

  /* Letterhead */
  .letterhead { left: 70px; top: 170px; width: 470px; height: 665px; }
  .letterhead .brand-mark { position: absolute; left: 34px; top: 30px; }
  .letterhead .brand-mark .dot { width: 54px; height: 54px; }
  .letterhead .brand-mark .name { font-size: 17px; }
  .letter-body { position: absolute; left: 120px; top: 130px; width: 300px; font-size: 8.6px; line-height: 1.5; }
  .letter-body .salutation { font-size: 15px; margin-bottom: 8px; }
  .letter-body p { margin-bottom: 11px; }
  .letterhead .web { position: absolute; right: 42px; top: 505px; font-size: 8px; }
  .letterhead .address-block { position: absolute; left: 34px; bottom: 30px; font-size: 7.5px; }

  /* Envelope front */
  .envelope-front { left: 610px; top: 130px; width: 480px; height: 240px; }
  .envelope-front .brand-mark { position: absolute; left: 22px; top: 22px; }
  .envelope-front .brand-mark .dot { width: 40px; height: 40px; }
  .envelope-front .brand-mark .name { font-size: 12px; }
  .envelope-front .contact { position: absolute; left: 22px; top: 72px; font-size: 6.5px; }
  .address-lines { position: absolute; right: 40px; top: 110px; width: 110px; }
  .address-lines span { display: block; height: 13px; border-bottom: 1px solid var(--rule); }

  /* Envelope back */
  .envelope-back { left: 610px; top: 400px; width: 480px; height: 240px; background: var(--envelope-back); }
  .envelope-back svg { position: absolute; inset: 0; }

  /* Business card */
  .business-card { left: 740px; top: 690px; width: 250px; height: 145px; }
  .business-card .brand-mark { position: absolute; left: 16px; top: 16px; }
  .business-card .brand-mark .dot { width: 30px; height: 30px; }
  .business-card .brand-mark .name { font-size: 10px; }
  .business-card .contact { position: absolute; right: 16px; top: 52px; text-align: right; font-size: 6.5px; }
</style>
</head>
<body>

<section class="sheet letterhead">
  <div class="brand-mark"><span class="dot"></span><span class="name">Cedar Hall</span></div>
  <div class="letter-body">
    <div class="salutation">Dear Mr. Lorem,</div>
    <p>Lorem ipsum dolor sit amet, consectetur adipiscing elit. Pellentesque ac dolor laoreet est pellentesque ornare ut vitae nulla. Mauris in eros nunc. Curabitur id odio aliquet, bibendum est in, facilisis mi. Suspendisse potenti. Morbi fermentum pretium felis, ac scelerisque sapien tempus et. Quisque vulputate mollis ex, in lacinia urna ultrices a. Sed dapibus imperdiet varius. Etiam magna elit, pulvinar vel sapien quis, convallis euismod turpis. Nam vitae ipsum sit amet justo sodales tincidunt. Class aptent taciti sociosqu ad litora torquent per conubia nostra, per inceptos himenaeos. Praesent nec risus nulla. Etiam justo ligula, condimentum vitae varius et, venenatis ac tellus. Quisque dignissim ac ante a cursus. Curabitur vitae mollis augue. Mauris non massa blandit, pharetra enim ac, egestas dui. Integer non nisl libero.</p>
    <p>Vestibulum eget egestas ipsum, nec convallis libero. Duis scelerisque et enim sit amet volutpat. Nullam sit amet est lorem. Vivamus sit amet iaculis libero. Suspendisse in semper nisl, non pharetra est. Curabitur sed euismod massa. Vivamus rutrum nunc sit amet lobortis vehicula. Aenean commodo convallis nisl in feugiat. Cras nec est sodales, scelerisque libero vel, fermentum arcu.</p>
    <p>Vestibulum eget egestas ipsum, nec convallis libero. Duis scelerisque et enim sit amet volutpat. Nullam sit amet est lorem. Vivamus sit amet iaculis libero. Suspendisse in semper nisl, non pharetra est. Curabitur sed euismod massa. Vivamus rutrum nunc sit amet lobortis vehicula. Aenean commodo convallis nisl in feugiat. Cras nec est sodales, scelerisque libero vel, fermentum arcu.</p>
    <p>Best regards,<br>Lorem Ipsum</p>
  </div>
  <div class="contact web">www.cedarhall.org.au</div>
  <div class="contact address-block">
    02 97584120<br>info@cedarhall.org.au<br>3-4/72 Harlow Street Rosedale 2199
  </div>
</section>

<section class="sheet envelope-front">
  <div class="brand-mark"><span class="dot"></span><span class="name">Cedar Hall</span></div>
  <div class="contact">
    3-4/72 Harlow Street Rosedale 2199<br>02 97584120<br>info@cedarhall.org.au<br>www.cedarhall.org.au
  </div>
  <div class="address-lines"><span></span><span></span><span></span><span></span></div>
</section>

<section class="sheet envelope-back">
  <svg width="480" height="240" viewBox="0 0 480 240" aria-hidden="true">
    <path d="M0 0 L0 20 Q0 40 30 42 L450 42 Q480 40 480 20 L480 0" fill="#8491a0" stroke="#6e7b88" stroke-width="1"/>
    <path d="M0 240 L70 60 Q80 44 100 44 L380 44 Q400 44 410 60 L480 240" fill="none" stroke="#6f7c89" stroke-width="1" opacity=".6"/>
  </svg>
</section>

<section class="sheet business-card">
  <div class="brand-mark"><span class="dot"></span><span class="name">Cedar Hall</span></div>
  <div class="contact">02 97584120<br>info@cedarhall.org.au<br>www.cedarhall.org.au</div>
</section>

</body>
</html>
```